RAmio Shop Business Card Design

My auto shop is targeted to the European and Asian luxury automotive market. We do mechanics collision and parts.
Some of the makes are KTR, DQ, Stone Herald, Valdine,Norvi, solavanta, bremo, HJ, etc. But in the end we get all makes.
I don't want to have the makes logos on the business card.
The Name of the business is after my first Name Ramiro but without the s Ramio Shop if there is any other ideas about the name iam open to suggestions. And i don't have a LOGO. Need logo!
Updates

Reason: I increased my budget and invited more designers. And committed payment so giving you guys more time.

Target Market(s)

target is the luxury auto market

Industry/Entity Type

Automotive

Contact Information for Business Card

European Automotive Repair Shop, Collision Mechanics Parts
Ramiro Villalba Owner, Colibrí #14 Loma Serena 2

Requirements
Nice to have
• One design i can of liked was the use of the dash error logos like check engine light airbag light. Nobla press has this but dose not include the air bag light. For the collision part of the business. But am open to any design.
Should not have
• exact logo makes on front of card.

```html
<!DOCTYPE html>
<html lang="en">
<head>
<meta charset="utf-8">
<title>Ramio Shop – Business Card</title>
<link href="https://fonts.googleapis.com/css2?family=PT+Sans:wght@400;700&display=swap" rel="stylesheet">
<style>
  :root {
    --bg-light: #ececec;
    --bg-dark: #c9c9c9;
    --wave-base: #b3d2ea;
    --wave-1: #8fbde0;
    --wave-2: #5f9fcf;
    --wave-3: #3c7fb2;
    --wave-deep: #1f5f8e;
    --icon-teal: #2a7f95;
    --card-white: #f7f7f7;
    --brand-navy: #26336e;
    --name-ink: #2b2b2b;
    --contact-grey: #8a8a8a;
  }
  * { margin: 0; padding: 0; box-sizing: border-box; }
  html, body { width: 1200px; height: 864px; overflow: hidden; }
  body {
    position: relative;
    background: linear-gradient(160deg, var(--bg-light) 0%, var(--bg-dark) 100%);
    font-family: "PT Sans", sans-serif;
  }
  .card {
    position: absolute;
    width: 500px;
    height: 290px;
    border-radius: 4px;
    overflow: hidden;
    box-shadow: 0 10px 24px rgba(0,0,0,0.22);
  }
  .card svg { position: absolute; inset: 0; width: 100%; height: 100%; }
  .card-front { left: 80px; top: 360px; }
  .card-back { left: 620px; top: 90px; background: var(--card-white); }

  .brand-name {
    position: absolute;
    font-family: "PT Sans", sans-serif;
    font-weight: 700;
    white-space: nowrap;
    line-height: 1;
  }
  .card-front .brand-name { left: 34px; top: 196px; font-size: 38px; color: #ffffff; }
  .card-back .brand-name { right: 34px; top: 40px; font-size: 28px; color: var(--brand-navy); }

  .holder-name {
    position: absolute;
    right: 34px; top: 104px;
    font-size: 26px;
    letter-spacing: 1.5px;
    color: var(--name-ink);
  }
  .contact-list {
    position: absolute;
    right: 34px; top: 150px;
    list-style: none;
    text-align: right;
    font-size: 16px;
    line-height: 1.3;
    color: var(--contact-grey);
  }
  .presentation-brand {
    position: absolute;
    right: 40px; bottom: 40px;
    font-size: 54px;
    font-weight: 700;
    color: var(--brand-navy);
  }
</style>
</head>
<body>

<section class="card card-front" aria-label="Business card front">
  <svg viewBox="0 0 500 290" preserveAspectRatio="none">
    <rect width="500" height="290" fill="var(--wave-base)"/>
    <path d="M250 0 C330 90 230 200 290 290 L500 290 L500 0 Z" fill="var(--wave-1)"/>
    <path d="M330 0 C400 100 320 200 390 290 L500 290 L500 0 Z" fill="var(--wave-2)"/>
    <path d="M420 0 C480 110 430 210 475 290 L500 290 L500 0 Z" fill="var(--wave-3)"/>
    <g class="icon-warning" transform="translate(178 62)" fill="var(--icon-teal)">
      <polygon points="0,-20 5,-9 17,-13 11,-2 21,5 9,7 8,19 0,11 -8,19 -9,7 -21,5 -11,-2 -17,-13 -5,-9"/>
      <rect x="-2" y="-9" width="4" height="11" fill="var(--wave-base)"/>
      <circle cx="0" cy="6" r="2.3" fill="var(--wave-base)"/>
    </g>
    <g class="icon-gear" transform="translate(308 108)" fill="var(--icon-teal)">
      <circle r="13"/>
      <g>
        <rect x="-3.5" y="-19" width="7" height="38"/>
        <rect x="-3.5" y="-19" width="7" height="38" transform="rotate(45)"/>
        <rect x="-3.5" y="-19" width="7" height="38" transform="rotate(90)"/>
        <rect x="-3.5" y="-19" width="7" height="38" transform="rotate(135)"/>
      </g>
      <circle r="7" fill="var(--wave-2)"/>
      <circle r="3.5"/>
    </g>
    <circle class="icon-team" cx="422" cy="132" r="18" fill="var(--icon-teal)" role="img" aria-label="Team icon"/>
  </svg>
  <span class="brand-name">Ramio Shop</span>
</section>

<section class="card card-back" aria-label="Business card back">
  <svg viewBox="0 0 500 290" preserveAspectRatio="none">
    <path d="M0 0 L235 0 C240 140 320 230 435 290 L0 290 Z" fill="#ffffff"/>
    <path d="M0 0 L225 0 C230 140 310 230 420 290 L0 290 Z" fill="var(--wave-deep)"/>
    <path d="M0 0 L190 0 C195 130 270 225 370 290 L0 290 Z" fill="var(--wave-3)"/>
    <path d="M0 0 L150 0 C160 125 220 220 310 290 L0 290 Z" fill="var(--wave-2)"/>
    <path d="M0 0 L105 0 C120 120 170 215 240 290 L0 290 Z" fill="var(--wave-1)"/>
    <path d="M0 0 L55 0 C75 110 110 210 160 290 L0 290 Z" fill="var(--wave-base)"/>
  </svg>
  <span class="brand-name">Ramio Shop</span>
  <p class="holder-name">ALEX MARLOW</p>
  <ul class="contact-list">
    <li>555 210 384</li>
    <li>name@ramiomail.com</li>
    <li>ramioshop-site.com</li>
  </ul>
</section>

<p class="presentation-brand brand-name">Ramio Shop</p>

</body>
</html>
```